Professional, Attractive, Simple Website Needed!!

We completed the design for our logo.

We need a website built out around this.

Here are a couple samples of how we want ours formatted.

http://brvtawatt.com

http://www.brightmerlo.com/lp/free-quote?LeadSource=Search%20Engine&ProgramName=webfind&experience=qual&language=en&type=brd&gclid=Xq7LMnvrTPKDWQAbZeRFtoPLmNcGxJbYTUWoKdMvCeWsfRgHyZnXpLoKqwErTyUiOpAsDfGhJkLzXcVb_zxwQ

http://qmorel.co

Project Deadline Extended
Reason: Extending this deadline due to our delay in providing designers with content for each page. This is coming in next 24 hours.

Project Deadline Extended
Reason: Due to scheduling conflicts and extended travel delays related to Puerto Rico, the deadline has been extended. Your patience is greatly appreciated.

Project Deadline Extended
Reason: Travel and scheduling conflicts have made it impossible to give this project the thorough review it deserves, therefore I am extending the deadline. Thank you for your patience!

Target Market(s)

Home Owners who earn 60k + household annually

Industry/Entity Type

It Professional

Coding

Coded - Design and coding required

Number of Pages Required

5+ page

Font styles to use
Serif

Colors
34a7d8
9bcb3c

Requirements
Must have
• Simple
• Lead form Entry (Ability for visitor to enter Name, number and address for a quote)
• Sleek Design
• Professional
• Testimonials
• Use color Scheme of Design Logo Attached
Nice to have
• Video when site starts
• Like this
• https://www.clipvault.com/watch?v=Rk8TpQwZmNe&feature=clipv.lt
Should not have
• Should not include Commercial solar
• Should not include wind power

```html
<!DOCTYPE html>
<html lang="en">
<head>
<meta charset="utf-8">
<title>Brightfield Power — Home</title>
<link rel="stylesheet" href="https://fonts.googleapis.com/css2?family=Roboto:wght@300;400;500;700&display=swap">
<style>
  :root {
    --brand-blue: #0b8fd0;
    --brand-green: #8dc63f;
    --ink: #222a33;
    --muted: #5b636b;
    --nav-ink: #1d232a;
    --pill-grey: #e3e8ee;
    --rule: #e6e9ec;
    --video-frame: #262626;
    --white: #ffffff;
  }
  * { box-sizing: border-box; margin: 0; padding: 0; }
  html, body { width: 1200px; height: 1200px; overflow: hidden; background: var(--white); }
  body { font-family: 'Roboto', sans-serif; color: var(--ink); position: relative; }

  .topbar { position: absolute; left: 0; top: 0; width: 1200px; height: 38px; background: var(--brand-blue); color: var(--white); font-size: 11px; }
  .topbar__item { position: absolute; top: 12px; display: flex; align-items: center; gap: 6px; }
  .topbar__item svg { width: 11px; height: 11px; }
  .topbar__social { position: absolute; right: 160px; top: 14px; display: flex; gap: 14px; }
  .topbar__social span { width: 9px; height: 9px; border-radius: 50%; background: var(--white); display: block; }

  .header { position: absolute; left: 0; top: 38px; width: 1200px; height: 75px; background: var(--white); }
  .brand { position: absolute; left: 159px; top: 24px; display: flex; align-items: center; gap: 7px; font-size: 16px; font-weight: 500; color: var(--brand-blue); }
  .brand__dot { width: 22px; height: 22px; border-radius: 50%; background: var(--brand-green); }
  .nav { position: absolute; top: 31px; font-size: 11px; font-weight: 500; color: var(--nav-ink); text-transform: uppercase; letter-spacing: .1px; }
  .nav--active { color: var(--brand-blue); }
  .nav--active::after { content: ""; position: absolute; left: 0; right: 0; top: 19px; height: 2px; background: var(--brand-blue); }
  .search { position: absolute; left: 1027px; top: 30px; width: 14px; height: 14px; }

  .hero { position: absolute; left: 0; top: 113px; width: 1200px; height: 528px;
    background: linear-gradient(180deg, #6f4a3c 0%, #d9612a 14%, #e86d22 34%, #5a3a2c 56%, #3b4a6a 74%, #2f4a86 100%); }
  .hero__title { position: absolute; left: 0; width: 1200px; top: 105px; text-align: center; font-size: 60px; line-height: 70px; font-weight: 400; color: var(--white); letter-spacing: .5px; }
  .hero__lead { position: absolute; left: 0; width: 1200px; top: 187px; text-align: center; font-size: 13.5px; line-height: 21px; font-weight: 300; color: var(--white); }
  .hero__cta { position: absolute; left: 513px; top: 257px; width: 173px; height: 34px; border-radius: 17px; background: var(--brand-green); color: var(--white); font-size: 13px; font-weight: 500; display: flex; align-items: center; justify-content: center; text-transform: uppercase; }
  .hero__arrow { position: absolute; top: 214px; width: 14px; height: 26px; }
  .hero__dots { position: absolute; left: 578px; top: 421px; display: flex; gap: 9px; }
  .hero__dots span { width: 8px; height: 8px; border-radius: 50%; border: 1.5px solid var(--white); }
  .hero__dots .is-current { background: var(--white); }

  .features { position: absolute; left: 158px; top: 569px; width: 881px; height: 269px; background: var(--white); box-shadow: 0 12px 30px rgba(0,0,0,.12); display: flex; }
  .feature { position: relative; flex: 1; text-align: center; }
  .feature + .feature::before { content: ""; position: absolute; left: 0; top: 73px; height: 122px; width: 1px; background: var(--rule); }
  .feature__icon { position: absolute; left: 50%; top: 34px; width: 28px; height: 30px; transform: translateX(-50%); }
  .feature__title { position: absolute; left: 0; right: 0; top: 83px; font-size: 18px; font-weight: 400; color: var(--ink); }
  .feature__text { position: absolute; left: 42px; right: 42px; top: 117px; font-size: 11px; line-height: 15.2px; font-weight: 300; color: var(--muted); }
  .feature__btn { position: absolute; left: 50%; top: 197px; width: 123px; height: 35px; transform: translateX(-50%); border-radius: 18px; background: var(--pill-grey); color: var(--nav-ink); font-size: 10px; font-weight: 500; display: flex; align-items: center; justify-content: center; text-transform: uppercase; }
  .feature__btn--primary { background: var(--brand-blue); color: var(--white); box-shadow: 0 8px 16px rgba(11,143,208,.3); }

  .video { position: absolute; left: 234px; top: 899px; width: 731px; height: 301px; background: var(--video-frame); }
  .video__screen { position: absolute; left: 80px; top: 10px; width: 569px; height: 291px;
    background: linear-gradient(180deg, #6d6d6d 0%, #f4f4f4 18%, #f1ece4 55%, #e7c178 100%); }
  .video__title { position: absolute; left: 8px; top: 7px; font-size: 12px; color: var(--white); }
  .video__tools { position: absolute; right: 10px; top: 8px; display: flex; gap: 10px; }
  .video__tools svg { width: 13px; height: 13px; }
</style>
</head>
<body>

<div class="topbar">
  <div class="topbar__item" style="left:158px">
    <svg viewBox="0 0 12 12" fill="#fff"><path d="M1 5c0-2 2-3 5-3s5 1 5 3v1H8V5H4v1H1z"/><rect x="2.5" y="6.5" width="7" height="4" rx="1"/></svg>
    1 (800) 555-0142
  </div>
  <div class="topbar__item" style="left:286px">
    <svg viewBox="0 0 12 12" fill="#fff"><path d="M1 2.5h10v7H1z"/><path d="M1 2.5l5 4 5-4" stroke="#0b8fd0" stroke-width="1" fill="none"/></svg>
    hello@brightfieldpower.com
  </div>
  <div class="topbar__social"><span></span><span></span><span></span></div>
</div>

<header class="header">
  <div class="brand"><span class="brand__dot"></span>Brightfield Power</div>
  <nav>
    <span class="nav nav--active" style="left:477px">Home</span>
    <span class="nav" style="left:543px">Why Choose Us</span>
    <span class="nav" style="left:663px">Join Our Team</span>
    <span class="nav" style="left:778px">Gallery</span>
    <span class="nav" style="left:859px">Social</span>
    <span class="nav" style="left:933px">Contact</span>
  </nav>
  <svg class="search" viewBox="0 0 14 14" fill="none" stroke="#0b8fd0" stroke-width="1.3"><circle cx="8" cy="6" r="4.5"/><path d="M4.8 9.2L1 13"/></svg>
</header>

<section class="hero" role="img" aria-label="Photo of a house with rooftop solar panels at sunset">
  <h1 class="hero__title">Pellentesque maximus</h1>
  <p class="hero__lead">Maecenas scelerisque tincidunt sapien eu placerat. Lorem ipsum dolor sit amet, consectetur adipiscing elit.<br>Nullam nisl lorem, blandit vitae malesuada vel, hendrerit quis lacus.</p>
  <div class="hero__cta">Schedule Now</div>
  <svg class="hero__arrow" style="left:136px" viewBox="0 0 14 26" fill="none" stroke="rgba(255,255,255,.6)" stroke-width="1.3"><path d="M12 1L2 13l10 12"/></svg>
  <svg class="hero__arrow" style="left:1050px" viewBox="0 0 14 26" fill="none" stroke="rgba(255,255,255,.6)" stroke-width="1.3"><path d="M2 1l10 12L2 25"/></svg>
  <div class="hero__dots"><span></span><span class="is-current"></span><span></span></div>
</section>

<section class="features">
  <article class="feature">
    <svg class="feature__icon" viewBox="0 0 28 30" fill="none" stroke="#0b8fd0" stroke-width="1.6"><circle cx="14" cy="12" r="9"/><path d="M9 9a6 6 0 0 1 5-4"/><path d="M5 20a12 12 0 0 0 18 0M14 23v5M9 28h10"/></svg>
    <h2 class="feature__title">Suspendisse potenti</h2>
    <p class="feature__text">Sed id rutrum risus, ac tempus mi. Praesent pretium volutpat tortor, vitae finibus ex viverra at. Fusce sed nunc congue dolor fringilla finibus at eget urna.</p>
    <div class="feature__btn">Learn More</div>
  </article>
  <article class="feature">
    <svg class="feature__icon" viewBox="0 0 28 30" fill="none" stroke="#0b8fd0" stroke-width="1.6"><rect x="1.5" y="5" width="25" height="22" rx="1"/><rect x="1.5" y="5" width="25" height="7" fill="#0b8fd0"/><path d="M8 1v7M20 1v7"/></svg>
    <h2 class="feature__title">Suspendisse potenti</h2>
    <p class="feature__text">Sed id rutrum risus, ac tempus mi. Praesent pretium volutpat tortor, vitae finibus ex viverra at. Fusce sed nunc congue dolor fringilla finibus at eget urna.</p>
    <div class="feature__btn feature__btn--primary">View All Event</div>
  </article>
  <article class="feature">
    <svg class="feature__icon" viewBox="0 0 28 30" fill="none" stroke="#0b8fd0" stroke-width="1.6"><path d="M3 9l17-6 2 6"/><rect x="2" y="9" width="24" height="19" rx="1"/><rect x="16" y="14" width="10" height="7" rx="1"/><circle cx="20" cy="17.5" r="1" fill="#0b8fd0"/></svg>
    <h2 class="feature__title">Suspendisse potenti</h2>
    <p class="feature__text">Sed id rutrum risus, ac tempus mi. Praesent pretium volutpat tortor, vitae finibus ex viverra at. Fusce sed nunc congue dolor fringilla finibus at eget urna.</p>
    <div class="feature__btn">Book Now</div>
  </article>
</section>

<section class="video">
  <div class="video__screen" role="img" aria-label="Animated explainer video about home solar with houses and a light bulb">
    <div class="video__title">Sunlight at Home</div>
    <div class="video__tools">
      <svg viewBox="0 0 13 13" fill="#fff"><path d="M8 2l5 4.5L8 11V8.5C4 8.5 2 10 1 12c0-4 2.5-7 7-7.5z"/></svg>
      <svg viewBox="0 0 13 13"><circle cx="6.5" cy="6.5" r="6" fill="#fff"/><path d="M6.5 5.5v4.5M6.5 3v1.2" stroke="#555" stroke-width="1.5"/></svg>
    </div>
  </div>
</section>

</body>
</html>
```